Beneath a Quiet Lantern (CD cover)

A CD cover that incorporates (if possible) a photo (or photos) with original art. (I'm flexible on this) Should have a sense of mystery... pensive, but also suggest expansiveness.

I'm open to putting photo on front of CD and art on back or inside, or vice versa, as I don't think they can be incorporated effectively??

I need a design primarily for the front, but possibly the back too (in other words, the sections that will be most visible prior to opening the CD.) This will be a "sleeve" or wallet style CD cover with 4 panels.

I'm including the liner notes, list of songs, artists, etc, but it's not necessary to lay that out too as that will be in the inside panels.

Target Market(s)

Jazz and independent/original music listeners

Industry/Entity Type

Artists

Requirements
Must have
• Cover:
Title of CD
My name
Names of band members
Photo or Art

Back or Inside:
Song titles
Photos of band and recording session
Introductory/explanatory verbiage
Nice to have
• Original art
Should not have
• No need to incorporate the liner notes attached - this was provided simply to give more information to designers - to give them more of a feel of what the album is about.

```html
<!DOCTYPE html>
<html lang="en">
<head>
<meta charset="utf-8">
<title>Beneath a Quiet Lantern – Back Traycard</title>
<link rel="stylesheet" href="https://fonts.googleapis.com/css2?family=Dancing+Script:wght@700&family=Roboto+Condensed:ital,wght@0,400;1,400;1,700&family=Playfair+Display:ital@1&family=Oswald:wght@700&display=swap">
<style>
  :root {
    --page: #ffffff;
    --gold-light: #fbe98a;
    --gold: #f6d21f;
    --amber: #e8a818;
    --rust: #8a4a14;
    --band: #3a2410;
    --ink: #3b2410;
    --number: rgba(120, 88, 48, 0.45);
    --quote-ink: #4a2810;
    --watermark: rgba(255, 255, 255, 0.12);
    --footer-ink: #fff8e6;
  }
  * { margin: 0; padding: 0; box-sizing: border-box; }
  html, body { width: 1200px; height: 1181px; overflow: hidden; background: var(--page); }
  .canvas { position: relative; width: 1200px; height: 1181px; }
  .traycard {
    position: absolute; left: 49px; top: 65px; width: 1102px; height: 946px; overflow: hidden;
  }
  .painted-ground {
    position: absolute; inset: 0;
    background:
      radial-gradient(ellipse 40% 22% at 78% 63%, rgba(255,250,225,.85), transparent 70%),
      radial-gradient(ellipse 60% 30% at 20% 55%, rgba(255,240,150,.55), transparent 70%),
      linear-gradient(180deg, var(--amber) 0%, var(--gold) 22%, var(--gold-light) 55%, var(--gold) 78%, var(--amber) 88%, var(--rust) 93%, var(--band) 100%);
  }
  .name-watermark {
    position: absolute; left: 10px; font-family: "Oswald", sans-serif; font-weight: 700;
    color: var(--watermark); line-height: 1; letter-spacing: 6px; white-space: nowrap;
  }
  .name-watermark.first { top: -30px; font-size: 330px; }
  .name-watermark.last { top: 300px; font-size: 300px; }
  .tracklist { list-style: none; }
  .track { position: absolute; left: 0; width: 640px; }
  .track-number {
    position: absolute; right: 536px; top: -14px; font-family: "Playfair Display", serif;
    font-style: italic; font-size: 54px; color: var(--number); line-height: 1;
  }
  .track-title {
    position: absolute; left: 108px; top: 0; font-family: "Roboto Condensed", sans-serif;
    font-size: 20px; color: var(--ink); line-height: 24px; white-space: nowrap;
  }
  .track-credit {
    position: absolute; left: 108px; top: 24px; font-family: "Roboto Condensed", sans-serif;
    font-style: italic; font-size: 16.5px; color: var(--ink); line-height: 23px; white-space: nowrap;
  }
  .quote-mark {
    position: absolute; left: 658px; top: 52px; font-family: "Playfair Display", serif;
    font-size: 190px; line-height: 1; color: rgba(120, 100, 80, 0.45);
  }
  .motto {
    position: absolute; left: 683px; top: 72px; font-family: "Dancing Script", cursive;
    font-weight: 700; font-size: 80px; line-height: 94px; color: var(--quote-ink);
    white-space: nowrap;
  }
  .portrait {
    position: absolute; left: 747px; top: 391px; width: 203px; height: 202px;
    background: radial-gradient(ellipse at 55% 45%, #9a958c, #3c3a36 60%, #151413);
  }
  .lineup {
    position: absolute; left: 620px; top: 637px; width: 456px; text-align: center;
    font-family: "Roboto Condensed", sans-serif; font-style: italic; font-size: 16.5px;
    line-height: 23px; color: var(--ink);
  }
  .lineup .guests { margin-top: 24px; }
  .footer-credits {
    position: absolute; left: 0; right: 0; top: 886px; text-align: center;
    font-family: "Roboto Condensed", sans-serif; font-style: italic; font-weight: 700;
    font-size: 16.5px; letter-spacing: 0.3px; color: var(--footer-ink); white-space: nowrap;
  }
  .panel-label {
    position: absolute; left: 0; right: 0; top: 1090px; text-align: center;
    font-family: "Roboto Condensed", Arial, sans-serif; font-size: 22px; color: #111;
  }
</style>
</head>
<body>
<div class="canvas">
  <section class="traycard">
    <div class="painted-ground" role="img" aria-label="Painted abstract background in golden yellow and amber brush strokes, fading to dark brown at the bottom"></div>
    <div class="name-watermark first">MARLA</div>
    <div class="name-watermark last">VENN</div>

    <ol class="tracklist">
      <li class="track" style="top:55px"><span class="track-number">1</span><span class="track-title">Hold On, We're Right Here</span><span class="track-credit">Marla Venn; Arranged by Otis Farrow</span></li>
      <li class="track" style="top:125px"><span class="track-number">2</span><span class="track-title">Autumn Field</span><span class="track-credit">Lionel Marsh – music, June Marsh – lyrics;<br>Arranged by Dale Corwin</span></li>
      <li class="track" style="top:219px"><span class="track-number">3</span><span class="track-title">Beneath a Quiet Lantern</span><span class="track-credit">Otis Farrow; Arranged by Otis Farrow</span></li>
      <li class="track" style="top:288px"><span class="track-number">4</span><span class="track-title">Just This, Just Now</span><span class="track-credit">Marla Venn; Arranged by Otis Farrow</span></li>
      <li class="track" style="top:358px"><span class="track-number">5</span><span class="track-title">Carnival*</span><span class="track-credit">Teddy Harlan; Arranged by Otis Farrow</span></li>
      <li class="track" style="top:428px"><span class="track-number">6</span><span class="track-title">Murmur</span><span class="track-credit">Marla Venn; Arranged by Otis Farrow</span></li>
      <li class="track" style="top:498px"><span class="track-number">7</span><span class="track-title">So Kind</span><span class="track-credit">Otis Farrow; Arranged by Otis Farrow</span></li>
      <li class="track" style="top:568px"><span class="track-number">8</span><span class="track-title">Bless the Little One**</span><span class="track-credit">Walter Brisk Jr &amp; Ida Pembrook; Arranged by Marla Venn</span></li>
      <li class="track" style="top:638px"><span class="track-number">9</span><span class="track-title">The Mere Idea of You</span><span class="track-credit">Roy Keller; Arranged by Otis Farrow &amp; Marla Venn</span></li>
      <li class="track" style="top:708px"><span class="track-number">10</span><span class="track-title">Overture to a Sigh</span><span class="track-credit">Earl Whitcombe; Arranged by Dale Corwin</span></li>
      <li class="track" style="top:777px"><span class="track-number">11</span><span class="track-title">Finer Than Everything</span><span class="track-credit">Dean Ashworth; Daniel Rye;<br>Arranged by Otis Farrow &amp; Marla Venn</span></li>
    </ol>

    <div class="quote-mark">“</div>
    <blockquote class="motto">Music is<br>the language<br>of the heart</blockquote>

    <div class="portrait" role="img" aria-label="Black and white portrait photo of the singer"></div>

    <div class="lineup">
      <p>Marla Venn - Voice | Dale Corwin - Piano<br>
      Skip Henley - Bass | Mark Ellery - Drums<br>
      Jay Porter - Trumpet, Flugelhorn, Tenor &amp; Soprano Sax<br>
      Jeff Tolan - Percussion | Dan Mercer - Guitar &amp; Banjo</p>
      <p class="guests">* Mike Daley - hand percussion on Carnival<br>
      * David Lorne - hand percussion on Carnival<br>
      * Otis Farrow - piano on Bless the Little One;<br>
      background vocals and hand percussion on Carnival</p>
    </div>

    <p class="footer-credits">Cover art by Ilsa Brandt | Produced by Otis Farrow, SMPA | Recorded at Lorne Hill Studios, Alder WA | Mastered by Ross Lindqvist, Kestrel Bay, WA.</p>
  </section>
  <p class="panel-label">BACK (TRAYCARD)</p>
</div>
</body>
</html>
```